Finally a Vodka produced for women ! (Label Design)

We are a small distillery based in Melbourne, Australia and we need a Vodka label design solution that will appeal to women aged 30-50 years and radiate luxury. Full Details are in a design brief attached. We thank you in advance.

Target Market(s)

Affluent females 30-50 years.

Industry/Entity Type

Spirits/Alcohol

Requirements
Must have
• Be clear this is a luxury Vodka.
Nice to have
• Elegance.

```html
<!DOCTYPE html>
<html lang="en">
<head>
<meta charset="utf-8">
<title>Silver Heron Distillery – Premium Vodka Label</title>
<link rel="stylesheet" href="https://fonts.googleapis.com/css2?family=Josefin+Sans:wght@400;600;700&family=Pinyon+Script&family=Montserrat:wght@500;600&display=swap">
<style>
  :root {
    --ink: #1b1917;
    --paper: #ffffff;
    --label-line: #d6d6d6;
    --rule: #6a6a6a;
    --quartz-light: #fbe6f0;
    --quartz-mid: #f2bfd6;
    --quartz-deep: #e9a6c4;
    --ornament: #e4e4e4;
  }
  * { margin: 0; padding: 0; box-sizing: border-box; }
  html, body { width: 1200px; height: 1041px; overflow: hidden; background: var(--paper); }
  .canvas { position: relative; width: 1200px; height: 1041px; background: var(--paper); color: var(--ink); }

  .brand-mark { position: absolute; left: 0; width: 1200px; top: 110px; text-align: center; }
  .brand-mark__dot { display: block; width: 64px; height: 64px; margin: 0 auto 38px; border-radius: 50%; background: var(--ink); }
  .brand-mark__name {
    font-family: "Josefin Sans", sans-serif; font-weight: 700; color: var(--ink);
    font-size: 38px; line-height: 40px; letter-spacing: 9px;
  }
  .brand-mark__name small { display: block; font-size: 15px; line-height: 22px; letter-spacing: 8px; }

  .label-outline { position: absolute; left: 0; top: 0; }

  .label__text { position: absolute; left: 412px; width: 362px; text-align: center; color: var(--ink); }
  .label__brand {
    top: 418px; font-family: "Josefin Sans", sans-serif; font-weight: 700;
    font-size: 31px; line-height: 32px; letter-spacing: 7px;
  }
  .label__brand small { display: block; font-size: 13px; line-height: 16px; letter-spacing: 7px; }
  .label__premium {
    top: 530px; font-family: "Josefin Sans", sans-serif; font-weight: 700;
    font-size: 24px; letter-spacing: 5px;
  }
  .label__product {
    top: 548px; font-family: "Pinyon Script", cursive; font-size: 128px; line-height: 170px;
  }

  .quartz-band {
    position: absolute; left: 429px; top: 731px; width: 331px; height: 42px;
    border-top: 1px solid var(--rule); border-bottom: 1px solid var(--rule);
    display: flex; align-items: center; justify-content: center;
  }
  .quartz-band__fill {
    position: absolute; left: 0; right: 0; top: 3px; bottom: 3px;
    background: linear-gradient(100deg, var(--quartz-mid), var(--quartz-light) 30%, var(--quartz-deep) 55%, var(--quartz-light) 80%, var(--quartz-mid));
    clip-path: polygon(0 50%, 4% 0, 96% 0, 100% 50%, 96% 100%, 4% 100%);
  }
  .quartz-band__text {
    position: relative; font-family: "Montserrat", sans-serif; font-weight: 500;
    font-size: 18px; letter-spacing: 0.5px; color: var(--ink);
  }

  .label__origin {
    top: 781px; font-family: "Josefin Sans", sans-serif; font-weight: 600;
    font-size: 11px; letter-spacing: 2.2px;
  }
  .label__spec {
    top: 803px; font-family: "Montserrat", sans-serif; font-weight: 600;
    font-size: 10px; line-height: 12px;
  }
  .rose-ornament {
    position: absolute; left: 525px; top: 834px; width: 133px; height: 35px;
    background: radial-gradient(ellipse at center, var(--ornament), rgba(228,228,228,0.2) 75%, transparent);
    border-radius: 50%;
  }
</style>
</head>
<body>
<main class="canvas">
  <header class="brand-mark">
    <span class="brand-mark__dot"></span>
    <p class="brand-mark__name">SILVER<br>HERON<small>DISTILLERY</small></p>
  </header>

  <svg class="label-outline" width="1200" height="1041" viewBox="0 0 1200 1041" aria-hidden="true">
    <polygon points="518,383 590,406 665,382 819,754 774,808 626,886 561,886 412,808 363,754"
             fill="var(--paper)" stroke="var(--label-line)" stroke-width="1"/>
  </svg>

  <section class="label">
    <p class="label__text label__brand">SILVER<br>HERON<small>DISTILLERY</small></p>
    <p class="label__text label__premium">PREMIUM</p>
    <p class="label__text label__product">Vodka</p>
    <div class="quartz-band">
      <span class="quartz-band__fill"></span>
      <span class="quartz-band__text">ROSE&nbsp; QUARTZ&nbsp; FILTERED</span>
    </div>
    <p class="label__text label__origin">HANDCRFTED IN MELBURNE, AUSTRALIA</p>
    <p class="label__text label__spec">40% ALC/VOL<br>700ml</p>
    <div class="rose-ornament" role="img" aria-label="Delicate line-drawn rose ornament"></div>
  </section>
</main>
</body>
</html>
```